Talbrook Business Card Design

We need to update our current company business cards to something that is more professional. We are oilfield equipment manufacturing company. The company has and will continue to use a logo that is similar to the KORVEN aspirin logo. I would like to see that used alone in the design because that is how most companies recognize us. I also would not mind seeing the logo designed into something more "oilfield" to add some identification to our product line (i.e. maybe a oil rig coming off of it or something). Our units are primarily red, so I would like to stick with a red, black, white, and maybe grey color scheme. In addition to our logo. Our NPQ logo should be on back of card similar to the one I am attaching (FENWICKS). I am in process of getting a clean copy of that image. I am attaching a card (FENWICKS) from a previous company that I worked at that is now closed that I like the design of. I have also attached a current business card.
Updates

I have added our logo and an old business card from a company no longer in existence that I really like the design of. Please use those items in design and a color scheme of red and black. Grey and white can also be incorporated if needed. I need a design that will also translate easily to letterhead, brochures, documents, etc. I plan on also having those designed when I find the right designer.

Industry/Entity Type

Business

Contact Information for Business Card

Front

Talbrook Services (and logo)

Marla Pritchett
Management Rep

361-574-8826 Phone
361-574-8829 Fax
361-430-6658 Mobile
mpritchett@talbrookrigworks.example

Back:
Corpus Christi - Headquarters
4190 Sparrow Ln.
Corpus Christi, TX 78316

Texas - North Dakota - Pennsylvania

www.talbrookrigworks.example

Colors
ec2027
000000
5c5c5c
ffffff

Requirements
Nice to have
• The owners do like cards that have an expensive look to them. They feel that they have achieved that previously with raised ink. That feature or something that separates this card from other would be nice.
Should not have
• This card should not be SUPER modern. This is still an "old school" type owned company. The card should be professional thou.

```html
<!DOCTYPE html>
<html lang="en">
<head>
<meta charset="utf-8">
<title>Talbrook Services Business Card</title>
<link rel="stylesheet" href="https://fonts.googleapis.com/css2?family=Open+Sans:wght@400;600;700;800&display=swap">
<style>
  :root {
    --red: #ec2027;
    --red-deep: #a3070c;
    --red-mid: #d0131a;
    --navy: #0f1120;
    --white: #ffffff;
    --stage: #e4e4e4;
    --divider: #9a9ca8;
  }
  * { margin: 0; padding: 0; box-sizing: border-box; }
  html, body { width: 1200px; height: 494px; overflow: hidden; }
  body {
    background: var(--stage);
    font-family: "Open Sans", Arial, sans-serif;
    position: relative;
  }
  .card {
    position: absolute;
    border-radius: 16px;
    overflow: hidden;
    box-shadow: 0 4px 12px rgba(0,0,0,0.25);
  }

  /* Front */
  .card-front { left: 38px; top: 30px; width: 556px; height: 318px; background: var(--white); }
  .brand-lockup {
    position: absolute; left: 0; top: 40px; width: 100%;
    display: flex; justify-content: center; align-items: center; gap: 12px;
  }
  .brand-dot {
    width: 34px; height: 34px; border-radius: 50%;
    border: 4px solid var(--red);
  }
  .brand-word {
    color: var(--red); font-weight: 800; font-size: 28px; line-height: 1; letter-spacing: 1px;
  }
  .company-name {
    position: absolute; left: 0; top: 108px; width: 100%;
    text-align: center;
    color: var(--red);
    font-weight: 800;
    font-size: 27px;
    letter-spacing: 0.5px;
    line-height: 1;
  }
  .contact-band {
    position: absolute; left: 0; top: 178px; width: 100%; height: 102px;
    background: var(--navy);
    color: var(--white);
    font-size: 14px;
  }
  .address {
    position: absolute; right: 300px; top: 16px;
    text-align: right; line-height: 22px; font-style: normal;
  }
  .address .web { display: inline-flex; align-items: center; gap: 6px; }
  .band-divider {
    position: absolute; left: 265px; top: 10px; width: 1px; height: 82px;
    background: var(--divider);
  }
  .numbers { position: absolute; left: 277px; top: 6px; list-style: none; line-height: 22px; }
  .numbers li { display: flex; align-items: center; gap: 8px; }
  .numbers svg { width: 13px; height: 13px; flex: none; }
  .name-band {
    position: absolute; left: 0; top: 280px; width: 100%; height: 38px;
    background: linear-gradient(180deg, var(--red-mid) 0%, var(--red-deep) 100%);
    color: var(--white);
    text-align: center; line-height: 38px;
  }
  .person-name { font-size: 17px; font-weight: 600; }
  .person-title { font-size: 14px; }

  /* Back */
  .card-back {
    left: 618px; top: 148px; width: 552px; height: 316px;
    background: radial-gradient(circle at 45% 40%, var(--red) 0%, var(--red-mid) 40%, var(--red-deep) 100%);
  }
  .back-lockup {
    position: absolute; left: 0; top: 100px; width: 100%;
    display: flex; justify-content: center; align-items: center; gap: 18px;
  }
  .back-dot {
    width: 60px; height: 60px; border-radius: 50%;
    border: 6px solid var(--white);
  }
  .back-word {
    color: var(--white); font-weight: 800; font-size: 44px; line-height: 1; letter-spacing: 1px;
  }
  .back-web {
    position: absolute; left: 0; top: 268px; width: 100%;
    text-align: center; color: var(--white);
    font-size: 13px; letter-spacing: 1.6px;
  }
</style>
</head>
<body>

<section class="card card-front" aria-label="Business card front">
  <div class="brand-lockup" aria-label="Talbrook">
    <span class="brand-dot" aria-hidden="true"></span>
    <span class="brand-word">TALBROOK</span>
  </div>
  <p class="company-name">TALBROOK SERVICES</p>

  <div class="contact-band">
    <address class="address">
      4190 Sparrow Ln.<br>
      Corpus Christi, TX 78316<br>
      <span class="web">
        <svg width="12" height="12" viewBox="0 0 12 12" aria-hidden="true"><circle cx="6" cy="6" r="5" fill="none" stroke="#fff" stroke-width="1"/><ellipse cx="6" cy="6" rx="2.2" ry="5" fill="none" stroke="#fff" stroke-width="1"/><line x1="1" y1="6" x2="11" y2="6" stroke="#fff"/></svg>
        www.talbrookrigworks.example
      </span>
    </address>
    <div class="band-divider"></div>
    <ul class="numbers">
      <li><svg viewBox="0 0 12 12" aria-hidden="true"><circle cx="6" cy="6" r="5.5" fill="none" stroke="#fff"/><path d="M4 3.2 L5 3 L5.6 4.6 L5 5.2 Q5.6 6.6 6.8 7 L7.4 6.4 L9 7 L8.8 8 Q6 8.6 4 5.6 Z" fill="#fff"/></svg>361 574 8826</li>
      <li><svg viewBox="0 0 12 12" aria-hidden="true"><rect x="3.5" y="0.5" width="5" height="11" rx="1" fill="none" stroke="#fff"/><rect x="4.5" y="2" width="3" height="4" fill="#fff"/></svg>361 430 6658</li>
      <li><svg viewBox="0 0 12 12" aria-hidden="true"><rect x="3" y="1" width="6" height="4" fill="none" stroke="#fff"/><rect x="1" y="5" width="10" height="6" rx="1" fill="#fff"/></svg>361 574 8829</li>
      <li><svg viewBox="0 0 12 12" aria-hidden="true"><rect x="0.5" y="2.5" width="11" height="8" fill="#fff"/><path d="M0.5 2.5 L6 7 L11.5 2.5" fill="none" stroke="var(--navy)"/></svg>mpritchett@talbrookrigworks.example</li>
    </ul>
  </div>

  <div class="name-band">
    <span class="person-name">Marla Pritchett,</span> <span class="person-title">Management Rep</span>
  </div>
</section>

<section class="card card-back" aria-label="Business card back">
  <div class="back-lockup" aria-label="Talbrook">
    <span class="back-dot" aria-hidden="true"></span>
    <span class="back-word">TALBROOK</span>
  </div>
  <p class="back-web">www.talbrookrigworks.example</p>
</section>

</body>
</html>
```